rk ironcraft business card metallic look

revamp the existing design but want card to have a metalic look to it

Target Market(s)

construction industry

Industry/Entity Type

constrction

Contact Information for Business Card

front of card RK Ironcraft, phone 4165550193, email rk.ironcraftt@veltrano.com and instagram account; rk_ironcraft_

Font styles to use
Other font styles liked:
• masculine

Colors

Designer to choose only greyscale colors for use in the design.

Requirements
Must have
• back side RK Ironcraft then a list of everything : Siding, ACM Panels, Standing Seam,Soffit, Fascia, Gutters,Metal,Alu,inum, Viynyl, Metal Roofs and roof repairs
Nice to have
• I would like to keep the look of the existing card with the metal grids on the front
Should not have
• Need a design in two days

```html
<!DOCTYPE html>
<html lang="en">
<head>
<meta charset="utf-8">
<title>RK Ironcraft – Business Card</title>
<link rel="stylesheet" href="https://fonts.googleapis.com/css2?family=Lato:wght@400;700;900&display=swap">
<style>
  :root {
    --page-bg: #ececec;
    --steel-light: #a4a4a4;
    --steel-mid: #6e6e6e;
    --steel-dark: #1c1c1c;
    --steel-deep: #2f2f2f;
    --steel-pale: #b0b0b0;
    --ink-white: #ffffff;
    --ghost-white: rgba(255, 255, 255, 0.28);
  }
  * { box-sizing: border-box; margin: 0; padding: 0; }
  html, body {
    width: 1098px;
    height: 1200px;
    overflow: hidden;
    background: var(--page-bg);
    font-family: "Lato", Arial, sans-serif;
  }
  .sheet {
    position: relative;
    width: 1098px;
    height: 1200px;
  }
  .card {
    position: absolute;
    left: 169px;
    width: 760px;
    height: 442px;
    overflow: hidden;
    box-shadow: 0 6px 18px rgba(0, 0, 0, 0.25);
  }
  .card--front { top: 120px; }
  .card--back { top: 640px; }

  .card__band-top {
    position: absolute;
    left: 0; top: 0; right: 0;
    background: linear-gradient(90deg, var(--steel-light) 0%, var(--steel-mid) 45%, var(--steel-dark) 100%);
  }
  .card__band-bottom {
    position: absolute;
    left: 0; right: 0; bottom: 0;
    background: linear-gradient(180deg, var(--steel-deep) 0%, var(--steel-mid) 45%, var(--steel-pale) 100%);
  }
  .card--front .card__band-top { height: 212px; }
  .card--front .card__band-bottom { top: 212px; }
  .card--back .card__band-top { height: 240px; }
  .card--back .card__band-bottom { top: 240px; }

  /* Front */
  .brand {
    position: absolute;
    left: 91px;
    top: 290px;
    color: var(--ink-white);
    font-weight: 900;
    line-height: 1;
  }
  .brand__initials { display: block; font-size: 66px; letter-spacing: 2px; }
  .brand__word { display: block; font-size: 22px; letter-spacing: 0.5px; margin-top: 2px; }

  .contacts {
    position: absolute;
    left: 346px;
    top: 287px;
    list-style: none;
    color: var(--ink-white);
    font-size: 22px;
    font-weight: 400;
  }
  .contacts__item {
    display: flex;
    align-items: center;
    height: 31px;
  }
  .contacts__icon {
    width: 20px;
    height: 20px;
    margin-right: 12px;
    flex: none;
  }

  /* Back */
  .ghost-brand {
    position: absolute;
    left: 0; right: 0;
    top: 22px;
    text-align: center;
    color: var(--ghost-white);
    font-weight: 900;
    line-height: 1;
  }
  .ghost-brand__initials { display: block; font-size: 140px; letter-spacing: 6px; }
  .ghost-brand__word { display: block; font-size: 50px; letter-spacing: 1px; margin-top: 6px; }

  .services {
    position: absolute;
    left: 20px; right: 20px;
    top: 300px;
    text-align: center;
    color: var(--ink-white);
    font-size: 17px;
    font-weight: 400;
    line-height: 32px;
    text-transform: uppercase;
  }
  .services strong { font-weight: 900; }
</style>
</head>
<body>
<main class="sheet">

  <section class="card card--front" aria-label="Business card front">
    <div class="card__band-top"></div>
    <div class="card__band-bottom"></div>

    <div class="brand">
      <span class="brand__initials">RK</span>
      <span class="brand__word">Ironcraft</span>
    </div>

    <ul class="contacts">
      <li class="contacts__item">
        <svg class="contacts__icon" viewBox="0 0 20 20" aria-hidden="true">
          <rect x="1" y="4" width="18" height="12" fill="#ffffff"/>
          <path d="M1.5 4.5 L10 11 L18.5 4.5" fill="none" stroke="#6e6e6e" stroke-width="1.6"/>
        </svg>
        rk.ironcraftt@veltrano.com
      </li>
      <li class="contacts__item">
        <svg class="contacts__icon" viewBox="0 0 20 20" aria-hidden="true">
          <circle cx="10" cy="10" r="7.5" fill="none" stroke="#ffffff" stroke-width="2"/>
        </svg>
        rk_ironcraft_
      </li>
      <li class="contacts__item">
        <svg class="contacts__icon" viewBox="0 0 20 20" aria-hidden="true">
          <circle cx="10" cy="10" r="10" fill="#ffffff"/>
          <path d="M6.3 4.8 L8.3 4.6 L9.2 7.4 L7.9 8.5 C8.6 10 9.9 11.4 11.5 12.1 L12.6 10.8 L15.4 11.7 L15.2 13.7 C14.9 14.8 13.8 15.4 12.7 15.1 C8.8 14 6 11.2 4.9 7.3 C4.6 6.2 5.2 5.1 6.3 4.8 Z" fill="#6e6e6e"/>
        </svg>
        416 555 0193
      </li>
    </ul>
  </section>

  <section class="card card--back" aria-label="Business card back">
    <div class="card__band-top"></div>
    <div class="card__band-bottom"></div>

    <div class="ghost-brand" aria-hidden="true">
      <span class="ghost-brand__initials">RK</span>
      <span class="ghost-brand__word">Ironcraft</span>
    </div>

    <p class="services">
      Siding| <strong>ACM Panels</strong>| Standing Seam| Soffit| Fascia| Gutters| Metal| Alu<br>
      inum| Viynyl |Metal Roofs | Roof Repairs
    </p>
  </section>

</main>
</body>
</html>
```